10 Page Marketing Report Template - Cindermoor Care Allies

https://www.vidquill.example/share/7f1e9c04b2d84a61a5c3e9d02b6f4a17

We are creating a professional, modern, and slightly edgy PDF-style report document (about 10 pages) to showcase the results of a client’s first 30 days with Cindermoor Care Allies.

The report will be designed as a customizable Plakkit template so the Client Success team can easily update logos, screenshots, and text for each client.

This document will serve as both a visual presentation piece and a report deliverable, blending clean design, modern layout, and data-driven storytelling.

I am attaching the content for the report doc and the design brief along with the logo.
Here is our website for design style, look, and feel: https://cindermoorcare.example/

Here is a quick overview video I made:

```html
<!DOCTYPE html>
<html lang="en">
<head>
<meta charset="utf-8">
<title>30 Days to Value Report – Cindermoor Care Allies</title>
<link rel="stylesheet" href="https://fonts.googleapis.com/css2?family=Montserrat:wght@500;600;800&family=Manrope:wght@400;500&display=swap">
<style>
  :root {
    --navy: #38475f;
    --navy-deep: #0d1a3d;
    --amber: #fbae17;
    --blue: #1c8fc8;
    --blue-dark: #0b3d63;
    --ink: #2f3b52;
    --paper: #ffffff;
    --backdrop: #e4e4e4;
  }
  * { margin: 0; padding: 0; box-sizing: border-box; }
  html, body { width: 1200px; height: 2344px; overflow: hidden; background: var(--backdrop); }
  .page {
    position: absolute; left: 232px; width: 734px; height: 1038px;
    background: var(--paper); overflow: hidden;
  }
  .page--cover { top: 81px; }
  .page--intro { top: 1200px; }
  .page svg.shapes { position: absolute; inset: 0; }
  .brand-name {
    position: absolute; font-family: "Montserrat", sans-serif; font-weight: 600;
    color: var(--ink); text-transform: uppercase; letter-spacing: 0.04em; line-height: 1.2;
  }
  .brand-mark { position: absolute; background: var(--amber); }
  .brand-tagline {
    position: absolute; font-family: "Montserrat", sans-serif; font-weight: 500;
    color: var(--ink); text-transform: uppercase; letter-spacing: 0.14em; white-space: nowrap;
  }
  .page--cover .brand-mark { left: 196px; top: 80px; width: 70px; height: 70px; }
  .page--cover .brand-name { left: 290px; top: 62px; font-size: 30px; }
  .page--cover .brand-tagline { left: 146px; top: 176px; font-size: 17px; }
  .cover-title {
    position: absolute; left: 0; right: 0; top: 700px; text-align: center;
    font-family: "Montserrat", sans-serif; font-weight: 800; color: #fff;
    font-size: 74px; line-height: 98px;
  }
  .cover-subtitle {
    position: absolute; left: 0; right: 0; top: 918px; text-align: center;
    font-family: "Manrope", sans-serif; font-weight: 500; color: #fff; font-size: 34px;
  }
  .page--intro .brand-mark { left: 50px; top: 62px; width: 40px; height: 40px; }
  .page--intro .brand-name { left: 112px; top: 50px; font-size: 18px; }
  .page--intro .brand-tagline { left: 50px; top: 118px; font-size: 10px; }
  .intro-copy {
    position: absolute; left: 50px; top: 216px; width: 640px;
    font-family: "Manrope", sans-serif; font-size: 20px; line-height: 26.5px; color: var(--ink);
  }
  .intro-copy p + p { margin-top: 26px; }
  .intro-visual {
    position: absolute; left: 0; top: 471px; width: 734px; height: 567px;
    background: radial-gradient(ellipse at 55% 65%, #1d5fb8 0%, #0f2c6e 40%, var(--navy-deep) 80%);
  }
</style>
</head>
<body>
  <section class="page page--cover">
    <svg class="shapes" width="734" height="1038" viewBox="0 0 734 1038">
      <defs>
        <linearGradient id="coverPhoto" x1="0" y1="0" x2="1" y2="1">
          <stop offset="0" stop-color="#27a8dc"/>
          <stop offset="0.5" stop-color="var(--blue)"/>
          <stop offset="1" stop-color="var(--blue-dark)"/>
        </linearGradient>
      </defs>
      <polygon points="0,90 384,479 0,756" fill="var(--amber)"/>
      <polygon points="199,259 734,356 734,820 393,479" fill="url(#coverPhoto)" role="img" aria-label="Photo of glowing blue bar chart with a rising arrow"/>
      <polygon points="0,781 399,491 734,838 734,1038 0,1038" fill="var(--navy)"/>
    </svg>
    <span class="brand-mark"></span>
    <div class="brand-name">Cindermoor<br>Care<br>Allies</div>
    <div class="brand-tagline">Driving growth. Redefining care.</div>
    <h1 class="cover-title">30 DAYS TO<br>VALUE REPORT</h1>
    <p class="cover-subtitle">Your First Month of Progress</p>
  </section>

  <section class="page page--intro">
    <svg class="shapes" width="734" height="1038" viewBox="0 0 734 1038">
      <polygon points="350,0 399,0 584,100 399,62" fill="var(--amber)"/>
      <polygon points="418,0 734,0 651,125" fill="var(--navy)"/>
    </svg>
    <span class="brand-mark"></span>
    <div class="brand-name">Cindermoor<br>Care Allies</div>
    <div class="brand-tagline">Driving growth. Redefining care.</div>
    <div class="intro-copy">
      <p>The first 30 days are about creating momentum. Our goal was to build the foundation for measurable growth — from your website and Mapwise Business Profile to your SEO systems, audits, and backlink strategy.</p>
      <p>This report highlights what’s been accomplished and what’s next in your marketing journey.</p>
    </div>
    <div class="intro-visual" role="img" aria-label="Digital illustration of glowing blue bar chart with an upward arrow"></div>
  </section>
</body>
</html>
```